載内容詳細に関しては、別添のExcel資料を参照してください。

・ターゲット
BtoB
木工架装を出来る業者を探している車のリース販売会社の担当様

・カラーイメージ
木目デザインと企業カラーである紺色を使用してデザインお願いします
▼木目参考
https://www.tomika-kobo.jp/
▼紺参考
https://www.rvm-t.jp/

・デザイン、ムード
木を扱う仕事なので、木目を上手く使ってデザインしてほしい
▼参考

・JQについて
JQのパターン制作は不要です。
1枚目の画像でデザインお願いします

配置やデザイン等はアレンジしていただいて構いません。
また、縦に制限はありません。

レスポンシブデザインのサイトで、bootstrap4を利用しコーディングする予定になります。

デザイン幅は2000px、コンテンツの幅はbootstrap4デフォルトのの1110pxを基準としてください。
ただし、最近のデザインの流行を取りいれて、フルワイドや、1200~15000px程度の幅のコンテンツをバランスよくレイアウトしてください。
コンテンツ配置は基本12分割になります。がデザインによっては、多少逸脱してもかまいません。
bootstrap4、12分割グリッドの基準のPSDも資料として添付しております。
ご参考になさってください。

本分のフォントはゴシック系は游ゴシック、メイリオ、明朝系は遊明朝でお願いします。
飾り文字はフリーフォントか、googleフォントを利用してください。

メイン画像部分・グローバルメニューは、ワイド適用でお願いします。

不明点、質問などありましたらメッセージ等でご連絡ください。
1ページ
青系、水色系
• 高解像度JPG (.jpg)
• フォトショップ形式 (.psd)
・資料上はサイト名(社名)や住所などは伏字にしております。
ご提案時点ではそのまま作成をお願いします。

・使用画像は当選後こちらで用意します。
ご提案時点では前項同様に、カンプデータ等をご使用のうえ、当選後に本内容へ差し替え修正をお願いします。
また、雰囲気が合っていれば、指定外の画像を追加掲載いただいてOKです。

・当選前提となった方は正式な社名及び連絡先をお伝えしますので修正対応をお願いします。
また希望の際は、当選後、中ページの制作及びコーディングも別途ご依頼可能です。

```html
<!DOCTYPE html>
<html lang="ja">
<head>
<meta charset="utf-8">
<title>Kisaragi Woodworking | 木工架装施工専門業者</title>
<link href="https://fonts.googleapis.com/css2?family=Noto+Sans+JP:wght@400;500;700&family=Noto+Serif+JP:wght@500;700&family=Great+Vibes&family=Montserrat:wght@500;600&display=swap" rel="stylesheet">
<style>
:root{
  --navy:#1c2c5b;
  --navy-dark:#142046;
  --wood-light:#d7b88e;
  --wood-mid:#b98a5c;
  --wood-dark:#6b4a30;
  --wood-deep:#4a3222;
  --paper:#ffffff;
  --grey:#f2f1ef;
  --ink:#333333;
  --muted:#777777;
}
*{box-sizing:border-box;margin:0;padding:0}
html,body{width:1200px;height:2352px;overflow:hidden}
body{position:relative;background:var(--paper);font-family:"Noto Sans JP",sans-serif;color:var(--ink)}
.abs{position:absolute}
.photo{position:absolute}

/* header */
.site-header{top:0;left:0;width:1200px;height:50px;background:var(--paper);box-shadow:0 1px 4px rgba(0,0,0,.08);z-index:5}
.header-tag{left:24px;top:10px;font-size:9px;color:var(--muted);line-height:1.4}
.header-tag strong{display:block;font-size:11px;color:var(--navy);font-weight:700;letter-spacing:.04em}
.brand{left:510px;top:9px;display:flex;align-items:center;gap:8px}
.brand-mark{width:30px;height:30px;background:var(--wood-dark)}
.brand-name{font-size:12px;font-weight:700;color:var(--wood-deep);letter-spacing:.04em}
.global-nav{right:24px;top:12px;display:flex;align-items:center;gap:22px;font-size:11px}
.global-nav a{color:var(--ink);text-decoration:none}
.nav-contact{background:var(--navy);color:#fff!important;padding:6px 16px;border-radius:2px}
.nav-tel{border:1px solid var(--navy);color:var(--navy)!important;padding:5px 14px;border-radius:2px;display:flex;align-items:center;gap:5px}

/* hero */
.hero{top:50px;left:0;width:1200px;height:590px;overflow:hidden}
.hero-wood{left:0;top:0;width:540px;height:590px;background:linear-gradient(90deg,#c7a072,#dcbf96 40%,#c39b6b 70%,#d4b285)}
.hero-van{left:520px;top:0;width:680px;height:590px;background:linear-gradient(135deg,#e8e6e2,#b9b5ae 35%,#c07a45 60%,#8e5630)}
.hero-label{left:0;top:150px;background:rgba(60,40,25,.85);color:#fff;font-size:22px;font-weight:700;padding:10px 26px 10px 40px;letter-spacing:.06em}
.hero-label span{font-weight:400;margin-left:14px;padding-left:14px;border-left:1px solid #fff}
.hero-copy{left:40px;top:208px;font-family:"Noto Serif JP",serif;font-size:30px;font-weight:700;color:#fff;line-height:1}
.hero-copy p{display:inline-block;background:var(--navy);padding:8px 14px;margin-bottom:6px}
.hero-script{left:40px;top:300px;font-family:"Great Vibes",cursive;font-size:48px;color:#fff;text-shadow:0 1px 3px rgba(0,0,0,.25)}

/* about */
.about{top:640px;left:0;width:1200px;height:560px;overflow:hidden}
.about-wood{left:600px;top:0;width:600px;height:560px;background:linear-gradient(180deg,#d9bd95,#c49e70 50%,#d1b083)}
.about-van{left:0;top:0;width:720px;height:520px;background:linear-gradient(160deg,#d9d7d3,#a8a39b 30%,#b7773f 55%,#8d5a32)}
.about-box{left:690px;top:70px;width:480px;background:var(--paper);padding:26px 28px 28px;box-shadow:0 2px 10px rgba(0,0,0,.12)}
.about-box h2{font-size:18px;color:var(--navy);font-weight:700;line-height:1.5;margin-bottom:6px}
.about-box .lead{font-size:11px;color:var(--muted);border-bottom:1px solid #ddd;padding-bottom:12px;margin-bottom:14px}
.about-box p{font-size:12px;line-height:1.9}
.about-script{left:30px;top:510px;font-family:"Great Vibes",cursive;font-size:40px;color:rgba(255,255,255,.7)}

/* business */
.business{top:1200px;left:0;width:1200px;height:380px;overflow:hidden}
.business-wood{left:0;top:0;width:620px;height:380px;background:linear-gradient(180deg,#7a5436,#5c3e28 50%,#6f4b30)}
.business-table{left:620px;top:0;width:580px;height:380px;background:linear-gradient(170deg,#d2cdc6,#b0a89d 40%,#a7683a 65%,#7b4a28)}
.business-card{left:32px;top:40px;width:150px;height:200px;background:var(--navy);padding:12px}
.business-card h3{color:#fff;font-size:16px;font-weight:700;border-bottom:1px solid rgba(255,255,255,.6);padding-bottom:6px;margin-bottom:10px}
.business-card .thumb{position:relative;width:126px;height:130px;background:linear-gradient(160deg,#c19063,#8c5d38)}
.business-text{left:210px;top:66px;width:360px;color:#fff;font-size:12px;line-height:1.9}
.btn{display:inline-block;background:var(--navy);color:#fff;font-size:12px;padding:9px 30px;text-decoration:none;border-radius:2px}
.business-btn{left:240px;top:160px}
.business-title{left:620px;top:95px;width:580px;text-align:center;font-family:"Montserrat",sans-serif;font-size:44px;font-weight:500;color:#fff;letter-spacing:.04em;text-shadow:0 1px 4px rgba(0,0,0,.3)}

/* works */
.works{top:1580px;left:0;width:1200px;height:410px;background:var(--grey);overflow:hidden}
.works-title{left:0;top:14px;width:1200px;text-align:center;font-size:16px;font-weight:700;color:var(--navy)}
.works-title span{display:inline-block;border-bottom:2px solid var(--navy);padding:0 10px 4px}
.works-grid{left:0;top:48px;width:1200px;display:grid;grid-template-columns:repeat(4,1fr);gap:8px}
.works-grid div{position:relative;height:150px}
.w1{background:linear-gradient(150deg,#cfccc7,#a2683c)}
.w2{background:linear-gradient(160deg,#e5e3df,#b7b2aa)}
.w3{background:linear-gradient(170deg,#8aa0b4,#9a6a42)}
.w4{background:linear-gradient(150deg,#d8d5d0,#a8703f)}
.w5{background:linear-gradient(160deg,#c9c6c0,#8f5e36)}
.w6{background:linear-gradient(150deg,#e0ddd8,#b28055)}
.w7{background:linear-gradient(160deg,#d2cfc9,#a57046)}
.w8{background:linear-gradient(150deg,#dcd9d4,#9b6a44)}
.works-btn{left:530px;top:366px;width:140px;text-align:center;padding:9px 0}

/* contact */
.contact{top:1990px;left:0;width:1200px;height:310px;overflow:hidden}
.contact-photo{left:0;top:0;width:600px;height:310px;background:linear-gradient(120deg,#e9e4dc,#cbb293 45%,#a57c55)}
.contact-script{left:60px;top:170px;font-family:"Great Vibes",cursive;font-size:64px;color:#fff;text-shadow:0 1px 4px rgba(0,0,0,.25)}
.contact-body{left:600px;top:0;width:600px;text-align:center;padding-top:62px}
.contact-body h2{font-size:18px;color:var(--navy);font-weight:700;margin-bottom:6px}
.contact-body .sub{font-size:11px;color:var(--muted);margin-bottom:22px}
.contact-btn{display:flex;align-items:center;justify-content:center;gap:8px;width:250px;height:36px;margin:0 auto 12px;font-size:13px;border-radius:2px}
.contact-tel{border:1px solid var(--navy);color:var(--navy)}
.contact-mail{background:var(--navy);color:#fff}

/* footer */
.site-footer{top:2300px;left:0;width:1200px;height:52px;background:linear-gradient(90deg,#4a3222,#6b4a30 50%,#4a3222);color:#fff}
.footer-brand{left:28px;top:12px;display:flex;align-items:center;gap:8px;font-size:12px;font-weight:700}
.footer-brand i{width:20px;height:20px;background:var(--wood-light)}
.footer-nav{right:28px;top:12px;display:flex;gap:22px;font-size:10px}
.copyright{left:0;top:36px;width:1200px;text-align:center;font-size:9px;color:rgba(255,255,255,.7)}
.pagetop{right:12px;top:-30px;width:24px;height:24px;background:var(--navy)}
</style>
</head>
<body>

<header class="site-header abs">
  <div class="header-tag abs">木工架装施工専門業者<strong>Kisaragi Woodworking</strong></div>
  <div class="brand abs"><span class="brand-mark"></span><span class="brand-name">KISARAGI</span></div>
  <nav class="global-nav abs">
    <a href="#">HOME</a>
    <a href="#">業務内容</a>
    <a href="#">施工事例</a>
    <a href="#" class="nav-contact">お問い合わせ</a>
    <a href="#" class="nav-tel"><svg width="10" height="10" viewBox="0 0 24 24"><path fill="#1c2c5b" d="M6.6 10.8a15 15 0 006.6 6.6l2.2-2.2a1 1 0 011-.25 11.4 11.4 0 003.6.6 1 1 0 011 1V20a1 1 0 01-1 1A17 17 0 013 4a1 1 0 011-1h3.5a1 1 0 011 1 11.4 11.4 0 00.6 3.6 1 1 0 01-.25 1z"/></svg>000-000-0000</a>
  </nav>
</header>

<section class="hero abs">
  <div class="photo hero-wood" role="img" aria-label="明るい木目の板の写真"></div>
  <div class="photo hero-van" role="img" aria-label="木工架装を施したバンの荷室の写真"></div>
  <div class="hero-label abs">木工架装施工専門業者<span>○○○○</span></div>
  <div class="hero-copy abs"><p>きめ細かいこだわりと</p><br><p>お客様のご要望を叶える確かな技術</p></div>
  <div class="hero-script abs">Kisaragi Woodworking</div>
</section>

<section class="about abs">
  <div class="photo about-wood" role="img" aria-label="木目の板の写真"></div>
  <div class="photo about-van" role="img" aria-label="木製の床を張ったバン荷室の写真"></div>
  <div class="about-box abs">
    <h2>車内の木工架装工事なら○○○○にご相談ください！</h2>
    <p class="lead">一台一台、丁寧な施工でお応えいたします。</p>
    <p>○○県○○市にある木工架装の専門業者です。創業以来、商用車の荷室へ床板や棚を取り付ける工事を数多く手掛けてまいりました。</p>
    <p>車両の用途やご予算に合わせて、最適な仕様をご提案いたします。まずはお気軽にお問い合わせください。</p>
  </div>
  <div class="about-script abs">Woodworking in Aichi</div>
</section>

<section class="business abs">
  <div class="photo business-wood" role="img" aria-label="濃い色の木目の写真"></div>
  <div class="photo business-table" role="img" aria-label="木製の作業台の写真"></div>
  <div class="business-card abs">
    <h3>業務内容</h3>
    <div class="thumb" role="img" aria-label="木材加工の写真"></div>
  </div>
  <p class="business-text abs">商用車を中心に木工架装を行っています。床張りから棚の製作まで、様々なご要望に対応いたします。施工期間は最短一日から承ります。</p>
  <a href="#" class="btn business-btn abs">業務内容</a>
  <div class="business-title abs">Business</div>
</section>

<section class="works abs">
  <h2 class="works-title abs"><span>施工事例</span></h2>
  <div class="works-grid abs">
    <div class="w1" role="img" aria-label="施工事例：荷室の床板"></div>
    <div class="w2" role="img" aria-label="施工事例：バンの外観"></div>
    <div class="w3" role="img" aria-label="施工事例：木製の荷台"></div>
    <div class="w4" role="img" aria-label="施工事例：荷室の内装"></div>
    <div class="w5" role="img" aria-label="施工事例：床板の仕上げ"></div>
    <div class="w6" role="img" aria-label="施工事例：側面パネル"></div>
    <div class="w7" role="img" aria-label="施工事例：荷室の棚"></div>
    <div class="w8" role="img" aria-label="施工事例：荷台の床"></div>
  </div>
  <a href="#" class="btn works-btn abs">すべて見る</a>
</section>

<section class="contact abs">
  <div class="photo contact-photo" role="img" aria-label="鉋で木材を削る手元の写真"></div>
  <div class="contact-script abs">contact</div>
  <div class="contact-body abs">
    <h2>お問い合わせ</h2>
    <p class="sub">ご依頼・ご相談はお気軽にお問い合わせください</p>
    <a class="contact-btn contact-tel"><svg width="13" height="13" viewBox="0 0 24 24"><path fill="#1c2c5b" d="M6.6 10.8a15 15 0 006.6 6.6l2.2-2.2a1 1 0 011-.25 11.4 11.4 0 003.6.6 1 1 0 011 1V20a1 1 0 01-1 1A17 17 0 013 4a1 1 0 011-1h3.5a1 1 0 011 1 11.4 11.4 0 00.6 3.6 1 1 0 01-.25 1z"/></svg>000-000-0000</a>
    <a class="contact-btn contact-mail"><svg width="14" height="12" viewBox="0 0 24 20"><rect x="1" y="1" width="22" height="18" fill="none" stroke="#fff" stroke-width="2"/><path d="M1 2l11 9 11-9" fill="none" stroke="#fff" stroke-width="2"/></svg>メールでのお問い合わせ</a>
  </div>
</section>

<footer class="site-footer abs">
  <span class="pagetop abs"></span>
  <div class="footer-brand abs"><i></i>Kisaragi Woodworking</div>
  <nav class="footer-nav abs"><span>HOME</span><span>業務内容</span><span>施工事例</span><span>お問い合わせ</span></nav>
  <p class="copyright abs">© Kisaragi Woodworking All Rights Reserved.</p>
</footer>

</body>
</html>
```